Brisk Science Academy by graduating students from college in two years

Based on the logo design, create stationary and business cards for
Dr. Velimir T Osunde, CEO, (555) 482-1630
and Mirela Thorpe, Respresentative, (555) 557-2048
Address: 4417 Marbleton Lane, Alderbrook Falls, OR 22061
Incorporate elelments of the logo

Target Market(s)

USA

Other font styles liked:
• match with the logo type style

```html
<!DOCTYPE html>
<html lang="en">
<head>
<meta charset="utf-8">
<title>Brisk Science Academy – Business Cards</title>
<link rel="stylesheet" href="https://fonts.googleapis.com/css2?family=Montserrat:wght@400;500;600&display=swap">
<style>
  :root {
    --page-bg: #ececec;
    --card-bg: #ffffff;
    --gold-light: #f8c431;
    --gold-mid: #e8b11b;
    --gold-dark: #c8961a;
    --navy: #14275e;
    --ink: #111111;
    --ink-soft: #222222;
    --white: #ffffff;
  }
  * { margin: 0; padding: 0; box-sizing: border-box; }
  html, body { width: 991px; height: 1200px; overflow: hidden; }
  body {
    background: radial-gradient(ellipse at center, #f4f4f4 0%, var(--page-bg) 100%);
    font-family: "Montserrat", sans-serif;
    position: relative;
  }
  .business-card {
    position: absolute;
    left: 96px;
    width: 799px;
    height: 466px;
    background: var(--card-bg);
    box-shadow: 0 4px 18px rgba(0,0,0,0.06);
    overflow: hidden;
  }
  .business-card--ceo { top: 117px; }
  .business-card--rep { top: 617px; }

  .brand {
    position: absolute;
    left: 41px;
    top: 100px;
    width: 240px;
    display: flex;
    flex-direction: column;
    align-items: center;
    gap: 16px;
  }
  .brand-dot {
    width: 64px; height: 64px;
    border-radius: 50%;
    background: var(--gold-light);
  }
  .brand-name {
    font-weight: 600;
    font-size: 21px;
    line-height: 1.25;
    color: var(--navy);
    text-align: center;
  }

  .person-name {
    position: absolute;
    left: 348px;
    top: 60px;
    font-weight: 600;
    font-size: 37px;
    line-height: 1.2;
    color: var(--ink);
    white-space: nowrap;
  }
  .person-title {
    position: absolute;
    left: 348px;
    font-weight: 400;
    font-size: 28px;
    line-height: 1.2;
    color: var(--ink-soft);
    white-space: nowrap;
  }
  .business-card--ceo .person-title { top: 110px; }
  .business-card--rep .person-title { top: 100px; }

  .contact-phone {
    position: absolute;
    left: 348px;
    top: 175px;
    display: flex;
    align-items: center;
    gap: 19px;
  }
  .phone-icon { width: 40px; height: 40px; display: block; }
  .phone-number {
    font-weight: 500;
    font-size: 30px;
    color: var(--ink);
  }

  .address-band {
    position: absolute;
    left: 0; top: 0;
    width: 799px; height: 466px;
  }
  .address-text {
    position: absolute;
    left: 0; right: 0;
    top: 399px;
    line-height: 1.2;
    text-align: center;
    font-weight: 600;
    font-size: 26px;
    color: var(--white);
    white-space: nowrap;
  }
</style>
</head>
<body>

  <section class="business-card business-card--ceo">
    <svg class="address-band" viewBox="0 0 1080 630" aria-hidden="true">
      <polygon points="0,515 395,470 685,470 1080,518 1080,630 0,630" fill="var(--gold-light)"/>
      <polygon points="350,470 377,418 395,470" fill="var(--gold-dark)"/>
      <polygon points="700,418 730,470 685,470" fill="var(--gold-dark)"/>
      <polygon points="377,418 700,418 665,515 415,515" fill="var(--gold-mid)"/>
      <path d="M538,433 a22,22 0 0 1 22,22 c0,15 -22,36 -22,36 c0,0 -22,-21 -22,-36 a22,22 0 0 1 22,-22 z" fill="var(--white)"/>
      <circle cx="538" cy="455" r="8" fill="var(--gold-mid)"/>
    </svg>
    <div class="brand">
      <div class="brand-dot"></div>
      <p class="brand-name">Brisk Science Academy</p>
    </div>
    <h1 class="person-name">Dr. Velimir T Osunde</h1>
    <p class="person-title">CEO</p>
    <div class="contact-phone">
      <svg class="phone-icon" viewBox="0 0 40 40" aria-hidden="true">
        <circle cx="20" cy="20" r="20" fill="var(--gold-light)"/>
        <path d="M13 11 l4 -1 l3 6 l-2.5 2 c1 2.5 3 4.5 5.5 5.5 l2 -2.5 l6 3 l-1 4 c-9 1 -18 -8 -17 -17 z" fill="var(--white)"/>
      </svg>
      <span class="phone-number">(555) 482-1630</span>
    </div>
    <p class="address-text">4417 Marbleton Lane, Alderbrook Falls, OR 22061</p>
  </section>

  <section class="business-card business-card--rep">
    <svg class="address-band" viewBox="0 0 1080 630" aria-hidden="true">
      <polygon points="0,515 395,470 685,470 1080,518 1080,630 0,630" fill="var(--gold-light)"/>
      <polygon points="350,470 377,418 395,470" fill="var(--gold-dark)"/>
      <polygon points="700,418 730,470 685,470" fill="var(--gold-dark)"/>
      <polygon points="377,418 700,418 665,515 415,515" fill="var(--gold-mid)"/>
      <path d="M538,433 a22,22 0 0 1 22,22 c0,15 -22,36 -22,36 c0,0 -22,-21 -22,-36 a22,22 0 0 1 22,-22 z" fill="var(--white)"/>
      <circle cx="538" cy="455" r="8" fill="var(--gold-mid)"/>
    </svg>
    <div class="brand">
      <div class="brand-dot"></div>
      <p class="brand-name">Brisk Science Academy</p>
    </div>
    <h1 class="person-name">Mirela Thorpe</h1>
    <p class="person-title">Respresentative</p>
    <div class="contact-phone">
      <svg class="phone-icon" viewBox="0 0 40 40" aria-hidden="true">
        <circle cx="20" cy="20" r="20" fill="var(--gold-light)"/>
        <path d="M13 11 l4 -1 l3 6 l-2.5 2 c1 2.5 3 4.5 5.5 5.5 l2 -2.5 l6 3 l-1 4 c-9 1 -18 -8 -17 -17 z" fill="var(--white)"/>
      </svg>
      <span class="phone-number">(555) 557-2048</span>
    </div>
    <p class="address-text">4417 Marbleton Lane, Alderbrook Falls, OR 22061</p>
  </section>

</body>
</html>
```